SIGN UP PAGE AND CHECK OUT PROCESS DESIGN NEEDED

I offer a subscription service. Two products that offer the same exact features just two different prices as the cheaper product offers limited of all the features....<br/><br/>PLEASE USE EXISTING THEME OF CURRENT DESIGN JUST MAKE AN IMPROVED SIGN UP PAGE. <br/><br/><br/>NEED SIGN UP PAGE for a subscription service..... <br/>This is my current sign up page, only offers one product: https://www.brightpromoperks.example/?page=signup <br/><br/>Please use all the same fields and content listed on this sign up page also please do a fake sign up to see the credit card page. I also need the credit card page to be designed....or if you want to combine the sign up and credit card page, etc. all in one I am open for that too....my goal is a super quick an easy sign up for customer. <br/><br/> AL A CARTE PROGRAM<br/>1 CERTIFICATE TYPE EACH MONTH<br/>$49/MTH MONTH TO MONTH BASIS NO CONTRACTS<br/>$239 ONE TIME PAYMENT FOR 6 MTHS OF SERVICE<br/>$399 ONE TIME PAYMENT FOR 12 MONTHS OF SERVICE<br/><br/>FEATURES:<br/><br/>UNLIMITED CERTIFICATE PDF DOWNLOADS<br/><br/>UNLIMITED E-MAIL CERTIFICATES<br/><br/>UNLIMITED TEXT/SMS CERTIFICATES<br/><br/>UNLIMITED API USAGE<br/><br/>UNLIMITED WEB BANNER CERTIFICATES<br/><br/>FULL REDEMPTION TRACKING<br/><br/>CERTIFICATE DISTRIBUTION REPORTS<br/><br/>WHITE LABEL REDEMPTION SITE<br/><br/>END USER MARKETING VIDEOS<br/><br/>MARKETING POSTERS AND FLYERS<br/><br/>PRODUCT DESCRIPTIONI BROCHURES<br/><br/>THE LATEST TIPS<br/><br/>SEPERATE REDEMPTION WEBSITES<br/><br/>CONTACT US 24/7<br/><br/>AFFILIATE PROGRAM<br/><br/>DISCOUNT TRAVEL BOOKING ENGINE<br/><br/>UNLIMITED PROGRAM<br/>UNLIMITED AMOUNTS OF ALL THE CERTIFICATES<br/>$99/MTH MONTH TO MONTH BASIS NO CONTRACTS<br/>$495 ONE TIME PAYMENT FOR 6 MTHS OF SERVICE<br/>$2,295 ONE TIME PAYMENT FOR 12 MONTHS OF SERVICE<br/><br/>FEATURES:<br/><br/>UNLIMITED CERTIFICATE PDF DOWNLOADS<br/><br/>UNLIMITED E-MAIL CERTIFICATES<br/><br/>UNLIMITED TEXT/SMS CERTIFICATES<br/><br/>UNLIMITED API USAGE<br/><br/>UNLIMITED WEB BANNER CERTIFICATES<br/><br/>FULL REDEMPTION TRACKING<br/><br/>CERTIFICATE DISTRIBUTION REPORTS<br/><br/>WHITE LABEL REDEMPTION SITE<br/><br/>END USER MARKETING VIDEOS<br/><br/>MARKETING POSTERS AND FLYERS<br/><br/>PRODUCT DESCRIPTIONI BROCHURES<br/><br/>THE LATEST TIPS<br/><br/>SEPERATE REDEMPTION WEBSITES<br/><br/>CONTACT US 24/7<br/><br/>AFFILIATE PROGRAM<br/><br/>DISCOUNT TRAVEL BOOKING ENGINE<br/><br/><br/>

Target Market(s)

B2B SMALL BUSINESS OWNERS
MARKETERS
ADVERTISERS

Industry/Entity Type

Digital Marketing

Number of Pages Required

3 page

Colors

Designer to choose colors to be used in the design.

Requirements
Must have
• MUST MATCH EXISTING THEME
Nice to have
• A VERY MODERN DESIGN

```html
<!DOCTYPE html>
<html lang="en">
<head>
<meta charset="utf-8">
<title>Sign Up – Bright Promo Perks</title>
<link href="https://fonts.googleapis.com/css2?family=Lato:wght@400;700;900&family=Montserrat:wght@600;700&display=swap" rel="stylesheet">
<style>
:root{
  --ink:#1c1c1c;
  --dark:#1e1e1e;
  --darker:#151515;
  --blue:#0a74c7;
  --grey:#9a9b9e;
  --line:#d3d3d3;
  --panel:#f7f7f7;
  --muted:#555;
  --white:#fff;
  --footer-text:#cfcfcf;
}
*{box-sizing:border-box;margin:0;padding:0}
html,body{width:806px;height:1200px;overflow:hidden;background:#fff}
body{position:relative;font-family:"Lato",sans-serif;color:var(--ink)}
.abs{position:absolute}
.site-header{left:0;top:0;width:806px;height:62px;background:var(--dark)}
.brand{left:162px;top:20px;display:flex;align-items:center;gap:5px;color:var(--blue);font-weight:900;font-size:13px;letter-spacing:.4px}
.brand .mark{width:14px;height:14px;background:var(--blue)}
.account-tabs{left:518px;top:0;height:17px;width:126px;display:flex;font-size:6.5px;color:#fff}
.account-tabs span{flex:1;display:flex;align-items:center;justify-content:center}
.tab-login{background:#3a3a3a;border-radius:0 0 0 6px}
.tab-signup{background:var(--blue);border-radius:0 0 6px 0}
.phone-badge{left:490px;top:29px;width:20px;height:20px;border-radius:50%;background:var(--blue);display:flex;align-items:center;justify-content:center}
.office{left:519px;top:28px;border-left:1px solid #555;padding-left:8px;color:#fff;font-size:8px;line-height:12.5px}
.office b{font-weight:700}
.main-nav{left:0;top:62px;width:806px;height:21px;background:var(--blue);display:flex;align-items:center;padding-left:170px;font-size:6.5px;color:#fff;font-weight:700}
.main-nav span{padding:0 15px;border-right:1px solid rgba(255,255,255,.25)}
.banner{left:0;top:83px;width:806px;height:64px;background:linear-gradient(100deg,#aab0d2 0%,#c7b6d2 45%,#e7bfc2 75%,#f7b89a 100%)}
.banner h1{position:absolute;width:100%;top:24px;text-align:center;color:#fff;font-size:14px;font-weight:400}
.steps-line{left:198px;top:209px;width:411px;height:1px}
.step{width:82px;height:82px;border-radius:50%;background:var(--grey);display:flex;align-items:center;justify-content:center}
.step.active{background:var(--blue)}
.step-label{width:120px;text-align:center;font-family:"Montserrat",sans-serif;font-weight:700;font-size:12px}
.intro{left:0;width:806px;text-align:center}
.intro p{font-size:9px}
.intro .warn{font-weight:700;font-size:9px;line-height:10.5px;margin-top:11px}
.card{background:var(--panel);border:1px solid #e2e2e2;box-shadow:0 0 3px rgba(0,0,0,.08)}
.summary{left:144px;top:387px;width:237px;height:200px;padding:14px 19px;font-size:6px;line-height:10px}
.summary .row{display:flex;justify-content:space-between}
.plan-title{font-weight:700;margin-top:2px}
.plans{display:flex;gap:8px;margin:2px 0 6px}
.plan{flex:1;border:1px solid #d6d6d6;background:#fff;padding:3px 5px;line-height:8.5px;font-size:5.4px}
.plan.selected{border-color:var(--blue)}
.plan b{display:block;font-size:5.6px;color:var(--ink)}
.opt{display:flex;align-items:center;gap:3px}
.opt i{width:5px;height:5px;border-radius:50%;border:1px solid #888;display:block}
.opt.on i{border-color:var(--blue);background:var(--blue)}
.billing{left:144px;top:598px;width:237px;height:305px;font-size:6px}
.field-label{position:absolute;left:20px}
.field{position:absolute;left:21px;width:199px;height:19px;background:#fff;border:1px solid #d6d6d6;font-size:6px;padding:6px 6px}
.field svg{position:absolute;right:7px;top:5px}
.cvv-note{position:absolute;left:20px;top:226px;width:205px;font-size:5.2px;line-height:10px;color:#333}
.terms-card{left:404px;top:387px;width:236px;height:516px}
.terms-box{position:absolute;left:13px;top:16px;width:209px;height:424px;border:1.5px solid #8a8a8a;padding:10px 6px 0 6px;font-size:5.1px;line-height:8.5px;color:#333}
.terms-box h2{font-size:10px;font-weight:400;line-height:12px;margin-bottom:3px;color:var(--ink)}
.terms-box h3{font-size:5.5px;font-weight:700;color:var(--ink);margin:0 0 8px}
.terms-box p{margin-bottom:8px}
.agree{position:absolute;left:15px;top:452px;font-size:5.5px;display:flex;align-items:center;gap:5px}
.agree i{width:6px;height:6px;border:1px solid #555;display:block}
.cta{position:absolute;left:14px;top:470px;width:209px;height:27px;background:var(--blue);color:#fff;font-weight:700;font-size:7.5px;display:flex;align-items:center;justify-content:center}
.site-footer{left:0;top:912px;width:806px;height:288px;background:var(--dark);color:var(--footer-text)}
.footer-title{font-size:9px;color:#fff}
.quick-links{left:162px;top:43px;font-size:6.3px;line-height:13.6px;list-style:none}
.quick-links li::before{content:"›";margin-right:4px}
.contact{left:328px;top:38px;font-size:5.8px;line-height:8.5px;color:#fff}
.contact .item{display:flex;gap:6px;margin-bottom:18px}
.divider{width:1px;height:120px;background:#2f2f2f}
.foot-brand{left:535px;top:22px;display:flex;align-items:center;gap:4px;color:var(--blue);font-weight:900;font-size:7.5px}
.foot-brand .mark{width:8px;height:8px;background:var(--blue)}
.social{left:555px;top:42px;display:flex;gap:4px}
.social span{width:15px;height:15px;border-radius:50%}
.copyright{left:0;top:1178px;width:806px;height:22px;background:var(--darker);color:#ddd;font-size:6px;text-align:center;line-height:22px}
</style>
</head>
<body>
<header class="abs site-header">
  <div class="abs brand"><span class="mark"></span>BRIGHT PROMO PERKS</div>
  <div class="abs account-tabs"><span class="tab-login">LOGIN</span><span class="tab-signup">SIGN UP</span></div>
  <div class="abs phone-badge"><svg width="9" height="9" viewBox="0 0 24 24"><path fill="#fff" d="M6.6 10.8a15 15 0 0 0 6.6 6.6l2.2-2.2c.3-.3.7-.4 1-.2 1.1.4 2.3.6 3.6.6.6 0 1 .4 1 1V20c0 .6-.4 1-1 1A17 17 0 0 1 3 4c0-.6.4-1 1-1h3.5c.6 0 1 .4 1 1 0 1.3.2 2.5.6 3.6.1.3 0 .7-.2 1z"/></svg></div>
  <div class="abs office">USA Office : <b>555-014-2290</b><br>International : <b>1-800-555-0188</b></div>
</header>
<nav class="abs main-nav"><span>HOME</span><span>OUR INCENTIVES</span><span>SAMPLES</span><span>AFFILIATES</span><span>TESTIMONIALS</span><span>FAQ</span><span>CONTACT</span></nav>
<section class="abs banner" role="img" aria-label="Soft pastel sky backdrop"><h1>SIGN UP</h1></section>

<svg class="abs steps-line" width="411" height="1" style="overflow:visible"><line x1="0" y1="0.5" x2="205" y2="0.5" stroke="#cfcfcf"/><line x1="205" y1="0.5" x2="411" y2="0.5" stroke="var(--blue)"/></svg>
<div class="abs step" style="left:157px;top:168px"><svg width="28" height="34" viewBox="0 0 28 34"><circle cx="14" cy="9" r="8" fill="#fff"/><path d="M0 34c0-9 6-15 14-15s14 6 14 15z" fill="#fff"/></svg></div>
<div class="abs step" style="left:362px;top:168px"><svg width="34" height="34" viewBox="0 0 34 34" fill="none" stroke="#fff" stroke-width="2.2"><path d="M18 4h10v10L14 30 4 20z"/><circle cx="24" cy="8" r="1.6"/><path d="M25 5l5-4"/><line x1="11" y1="21" x2="19" y2="17"/><circle cx="13" cy="17" r="1.3"/><circle cx="17" cy="22" r="1.3"/></svg></div>
<div class="abs step active" style="left:568px;top:168px"><svg width="32" height="24" viewBox="0 0 32 24" fill="none" stroke="#fff" stroke-width="2.2"><rect x="1" y="1" width="30" height="22" rx="3"/><line x1="1" y1="8" x2="31" y2="8"/><circle cx="8" cy="16" r="2"/><line x1="14" y1="16" x2="26" y2="16"/></svg></div>
<div class="abs step-label" style="left:138px;top:258px">STEP 1</div>
<div class="abs step-label" style="left:343px;top:258px">STEP 2</div>
<div class="abs step-label" style="left:549px;top:258px">STEP 3</div>

<div class="abs intro" style="top:316px"><p>Please verify your enter your credit card info bellow</p><p class="warn">**The information you provider below must match the billing details of<br>where your billing statement is mailed to from your bank.</p></div>

<section class="abs card summary">
  <div>Jordan Reyes</div><div>1200 Maple Lane</div><div>&nbsp;</div><div>Oakdale, CA 90012</div><div>US</div><div>5550123456</div><div>jordan@example.com</div><div>Username:jreyes</div>
  <div class="plan-title">Choose Your Program</div>
  <div class="plans">
    <div class="plan"><b>AL A CARTE PROGRAM</b>
      <div class="opt"><i></i>$49/mth month to month</div>
      <div class="opt"><i></i>$239 one time, 6 mths</div>
      <div class="opt"><i></i>$399 one time, 12 mths</div>
    </div>
    <div class="plan selected"><b>UNLIMITED PROGRAM</b>
      <div class="opt on"><i></i>$99/mth month to month</div>
      <div class="opt"><i></i>$495 one time, 6 mths</div>
      <div class="opt"><i></i>$2,295 one time, 12 mths</div>
    </div>
  </div>
  <div class="row"><span>One-Time Set Up Fee:</span><span>$99.00</span></div>
  <div class="row"><span>Monthly Fee:</span><span>$99.00/Month</span></div>
  <div class="row"><span>Total Charger Today</span><span>$198.00</span></div>
</section>

<section class="abs card billing">
  <div class="field-label" style="top:19px">Credit Card Type</div>
  <div class="field" style="top:29px">Select One<svg width="6" height="4" viewBox="0 0 6 4"><path d="M0 0l3 3 3-3" fill="none" stroke="#555" stroke-width=".8"/></svg></div>
  <div class="field-label" style="top:58px">Credit Card No #</div>
  <div class="field" style="top:68px"></div>
  <div class="field-label" style="top:98px">Credit Card Exp Month</div>
  <div class="field" style="top:108px">01<svg width="6" height="4" viewBox="0 0 6 4"><path d="M0 0l3 3 3-3" fill="none" stroke="#555" stroke-width=".8"/></svg></div>
  <div class="field-label" style="top:139px">Credit Card Exp Year</div>
  <div class="field" style="top:149px">2019<svg width="6" height="4" viewBox="0 0 6 4"><path d="M0 0l3 3 3-3" fill="none" stroke="#555" stroke-width=".8"/></svg></div>
  <div class="field-label" style="top:181px">Credit Card CVV2</div>
  <div class="field" style="top:191px"></div>
  <div class="cvv-note">The CVV2 is the three digit code on the signature panel of CardOne, PayMax or Cardora after the card number.<br>On Amerix Card it is the four digit code printed above the credit card number on the front the card.</div>
</section>

<section class="abs card terms-card">
  <div class="terms-box">
    <h2>Payment Terms and Conditions</h2>
    <h3>$99 Recurring Billing</h3>
    <p>You must provide a valid billing method. BPPG will immediately charge your account $198. BPPG will continue to debit your account automatically every month for $99. This process will remain in full force until BPPG receives a cancellation notice through the online support ticket system, conveniently located in your password protected control panel area. We must receive the cancellation notice a minimum of 3 business days (not counting holidays or weekends) prior to your next billing date in order to avoid being billed for the following month. Business days are Monday through Friday only, and do not include holidays or weekends.</p>
    <h3>Refund Policy</h3>
    <p>We provide a 3-day refund policy. We will refund you 100%, provided that you request your refund within 3 days of your initial enrollment date. We pay our vendors after 3 days for every member. Therefore, we cannot honor or authorize refund requests after 3 days for reimbursement, as we have already forwarded that money to our clients.</p>
    <h3>30 Day Risk-Free Trial Terms &amp; Conditions</h3>
    <p>Our incentive marketing program works and we are willing to prove that it works at no risk to our new customers.</p>
    <p>Our incentives work but there is participation required by our customers; you must run incentive marketing campaigns within your business to receive your desired results.</p>
    <p>Therefore to participate and to receive the refund you must use our service in the first 30 days from your membership sign up date. To qualify for the 30 day risk free trial refund you need to have at least one (1) paid redemption in the first 30 days of your membership. Redeeming a "Free Healthcare Discount Card" does not satisfy your requirement because it is not a "paid redemption."</p>
    <p>If you are not completely satisfied with the redemption and or the fulfillment process within the first 30 days we will refund 100% of your membership fees per your request.</p>
  </div>
  <div class="agree"><i></i>I agree to the Payment Term and Condition.</div>
  <div class="cta">SIGN UP NOW</div>
</section>

<footer class="abs site-footer">
  <div class="abs footer-title" style="left:162px;top:26px">QUICK LINKS</div>
  <ul class="abs quick-links">
    <li>Home</li><li>Our Incentives</li><li>Samples</li><li>Affiliate</li><li>Testimonials</li><li>Faq</li><li>Contact Us</li><li>Terms &amp; Conditions</li><li>Privacy Policy</li><li>Hoteliers</li><li>BPP PDF Flyer</li><li>BPP PDF Brochure</li><li>BPP Certificates List</li><li>How To Use BPP Certificates</li><li>Free Video Ad Mock Up For Marketing</li>
  </ul>
  <div class="abs divider" style="left:321px;top:26px"></div>
  <div class="abs divider" style="left:528px;top:26px"></div>
  <div class="abs footer-title" style="left:328px;top:26px">CONTACT DETAILS</div>
  <div class="abs contact">
    <div class="item"><svg width="6" height="8" viewBox="0 0 12 16"><path d="M6 0a6 6 0 0 0-6 6c0 4.5 6 10 6 10s6-5.5 6-10a6 6 0 0 0-6-6zm0 8.5A2.5 2.5 0 1 1 6 3.5a2.5 2.5 0 0 1 0 5z" fill="#ddd"/></svg><div><b>Bright Promo Perks Group, Inc.</b><br><span style="line-height:11px">4470 Harbor View Road<br>Bayside CA 90001</span></div></div>
    <div class="item"><svg width="8" height="8" viewBox="0 0 16 16" fill="none" stroke="#ddd" stroke-width="1.4"><rect x="1" y="3" width="14" height="12"/><line x1="1" y1="7" x2="15" y2="7"/><line x1="5" y1="1" x2="5" y2="4"/><line x1="11" y1="1" x2="11" y2="4"/></svg><div>Hours: Mon-Fri 8am - 5pm PST<br>Sat-Sun CLOSED</div></div>
  </div>
  <div class="abs foot-brand"><span class="mark"></span>BRIGHT PROMO PERKS</div>
  <div class="abs social"><span style="background:#3b5998"></span><span style="background:#e52d27"></span><span style="background:#0a66c2"></span><span style="background:#2d8ff0"></span></div>
</footer>
<div class="abs copyright">Copyright 2005-2020 Bright Promo Perks Group, Inc. All Rights Reserved.</div>
</body>
</html>
```